web page layout, style , color, font & flow design

We are developing a single page application. The SPA (single page application) will display natural gas pipeline flow data once the customer logs on. The customer has a choice of the region, the pipeline, the zone on the pipeline, whether the point is a delivery point or receipt point and the state the pipeline flows through.
we have jumpstarted the project and are attaching a pdf of the same.

we are using mockingbird for the wireframe. any designer is free to use this tool to make changes.

A mockingbird wireframe link is added below. you are free to use it and to make changes. please save the changed wireframe in a different name

we are looking for inputs on layout, style , color, font & flow.

A logo jpg file has also been attached.

Target Market(s)

this single web page is going to be used by natural gas traders and schedulers day in and day out. the application is more of business to business corporate application.

Industry/Entity Type

Delivery

Requirements
Must have
• layout ,flow, size, color, font , ease of use.

```html
<!DOCTYPE html>
<html lang="en">
<head>
<meta charset="utf-8">
<title>Wholesale NG Supply Analysis</title>
<link rel="stylesheet" href="https://fonts.googleapis.com/css2?family=Arimo:wght@400;700&display=swap">
<style>
  :root{
    --bg-dark:#1c2224;
    --bg-mid:#3a4447;
    --bar:#4f6b70;
    --bar-active:#6b8f95;
    --panel:#678a90;
    --side-panel:#52707a;
    --field:#a8bec0;
    --field-text:#7b9499;
    --arrow-box:#253234;
    --row-light:#7fa1a5;
    --row-dark:#6f9196;
    --grid-line:#a9c1c3;
    --list-text:#b3c6c8;
    --white:#ffffff;
    --title:#d6dcdd;
    --tab-text:#1d2a2c;
  }
  *{box-sizing:border-box;margin:0;padding:0}
  html,body{width:1200px;height:811px;overflow:hidden}
  body{font-family:"Arimo",Arial,sans-serif;position:relative;background:var(--bg-dark)}
  .backdrop{position:absolute;inset:0;background:radial-gradient(ellipse at 55% 40%,#4c5759 0%,var(--bg-mid) 35%,var(--bg-dark) 100%)}
  .logout{position:absolute;right:27px;top:15px;color:var(--white);font-size:13px;text-decoration:none}
  .brand{position:absolute;left:27px;top:37px;width:98px;height:83px;background:var(--white);display:flex;align-items:center;justify-content:center;gap:5px;font-size:13px;font-weight:700;color:#2f3d40}
  .brand-dot{width:10px;height:10px;border-radius:50%;background:#4f9ad1}
  .page-title{position:absolute;left:0;right:0;top:58px;padding-left:62px;text-align:center;font-size:30px;font-weight:400;color:var(--title);text-shadow:1px 2px 2px #000}
  .filters{position:absolute;left:25px;top:152px;width:1150px;height:181px;background:var(--panel)}
  .regions{display:flex;height:52px;background:var(--bar);list-style:none}
  .regions li{flex:1;display:flex;align-items:center;justify-content:center;font-size:17px;color:var(--tab-text)}
  .regions li:first-child{flex:0 0 191px}
  .regions li.active{background:var(--bar-active);color:var(--white)}
  .select{position:absolute;width:268px;height:33px;background:var(--field);color:var(--field-text);font-size:17px;line-height:33px;padding-left:9px}
  .select::after{content:"";position:absolute;right:5px;top:6px;width:27px;height:21px;background:var(--arrow-box)}
  .select svg{position:absolute;right:11px;top:13px;z-index:1}
  .submit{position:absolute;left:1019px;top:127px;width:99px;height:37px;border:1px solid var(--arrow-box);background:transparent;color:#3a4d50;font:17px "Arimo",Arial,sans-serif}
  .pipelines{position:absolute;left:25px;top:367px;width:304px;height:402px;background:var(--side-panel);list-style:none;padding-top:37px;padding-left:34px}
  .pipelines li{font-size:16px;line-height:21.3px;color:var(--list-text);white-space:nowrap}
  .pipelines li.active{color:var(--white)}
  .results{position:absolute;left:357px;top:367px;width:818px;height:402px;background:var(--panel)}
  .flow-table{position:absolute;left:35px;top:36px;border-collapse:collapse;table-layout:fixed;width:748px}
  .flow-table th,.flow-table td{border:1px solid var(--grid-line);font-size:14px;color:var(--white);text-align:left;padding-left:4px}
  .flow-table th{height:52px;font-weight:400;font-size:13px;background:var(--panel)}
  .flow-table td{height:33px;font-size:16px;padding-left:10px}
  .flow-table tbody tr:nth-child(odd){background:var(--row-dark)}
  .flow-table tbody tr:nth-child(even){background:var(--row-light)}
  .flow-table tbody tr:last-child td{height:52px}
</style>
</head>
<body>
  <div class="backdrop" role="img" aria-label="Dark industrial photograph of gas pipework and valves"></div>

  <a class="logout" href="#">LOGOUT</a>
  <div class="brand"><span class="brand-dot"></span>Ferrovane</div>
  <h1 class="page-title">Wholesale NG Supply Analysis</h1>

  <section class="filters">
    <ul class="regions">
      <li class="active">NORTH EAST</li>
      <li>MID WEST</li>
      <li>SOUTH EAST</li>
      <li>SOUTH WEST</li>
      <li>CENTRAL</li>
      <li>WEST</li>
    </ul>
    <div class="select" style="left:30px;top:75px">Location type<svg width="14" height="8" viewBox="0 0 14 8"><path d="M0 0h14L7 8z" fill="#a8bec0"/></svg></div>
    <div class="select" style="left:332px;top:75px">States<svg width="14" height="8" viewBox="0 0 14 8"><path d="M0 0h14L7 8z" fill="#a8bec0"/></svg></div>
    <div class="select" style="left:636px;top:75px">Zones<svg width="14" height="8" viewBox="0 0 14 8"><path d="M0 0h14L7 8z" fill="#a8bec0"/></svg></div>
    <div class="select" style="left:30px;top:127px">Gas Day<svg width="14" height="8" viewBox="0 0 14 8"><path d="M0 0h14L7 8z" fill="#a8bec0"/></svg></div>
    <div class="select" style="left:332px;top:127px">Cycle<svg width="14" height="8" viewBox="0 0 14 8"><path d="M0 0h14L7 8z" fill="#a8bec0"/></svg></div>
    <div class="select" style="left:636px;top:127px">Posting Time<svg width="14" height="8" viewBox="0 0 14 8"><path d="M0 0h14L7 8z" fill="#a8bec0"/></svg></div>
    <button class="submit" type="button">SUBMIT</button>
  </section>

  <ul class="pipelines">
    <li>Alderbrook</li>
    <li>KRT</li>
    <li>Dunhallow</li>
    <li>Harbor Coast NG</li>
    <li>East Ridgeway NG</li>
    <li class="active">Kestrel Gas</li>
    <li>Lumaridge Inc</li>
    <li>Slate Valley Gas</li>
    <li>Ossinaw</li>
    <li>Coastal &amp; North East</li>
    <li>Brightwater Pipeline</li>
    <li>Northvale Fuel Gas Supply Co</li>
    <li>Bayport NG</li>
    <li>St.Clairmont Gas</li>
    <li>Tamberlin Gas</li>
    <li>Tovrex</li>
  </ul>

  <section class="results">
    <table class="flow-table">
      <colgroup>
        <col style="width:81px"><col style="width:84px"><col style="width:90px"><col style="width:92px">
        <col style="width:104px"><col style="width:101px"><col style="width:100px"><col style="width:96px">
      </colgroup>
      <thead>
        <tr><th>Gas Day</th><th>Location</th><th>Loc_Name</th><th>Flow_Ind</th><th>Loc_Desc</th><th>Op_Cap</th><th>Sch_Cap</th><th>Op_avail_cap</th></tr>
      </thead>
      <tbody>
        <tr><td>Data1</td><td>Data2</td><td></td><td></td><td></td><td></td><td></td><td></td></tr>
        <tr><td>Data3</td><td>Data4</td><td></td><td></td><td></td><td></td><td></td><td></td></tr>
        <tr><td></td><td></td><td></td><td></td><td></td><td></td><td></td><td></td></tr>
        <tr><td></td><td></td><td></td><td></td><td></td><td></td><td></td><td></td></tr>
        <tr><td></td><td></td><td></td><td></td><td></td><td></td><td></td><td></td></tr>
        <tr><td></td><td></td><td></td><td></td><td></td><td></td><td></td><td></td></tr>
        <tr><td></td><td></td><td></td><td></td><td></td><td></td><td></td><td></td></tr>
        <tr><td></td><td></td><td></td><td></td><td></td><td></td><td></td><td></td></tr>
      </tbody>
    </table>
  </section>
</body>
</html>
```